Ferris Contracting LLC Business Card Design

I am looking for a creative and unique business card design. We are a commercial construction general contractor. With the name "FERRIS" Contracting, I am hoping to see some neat designs that correlate with the name.

```html
<!DOCTYPE html>
<html lang="en">
<head>
<meta charset="utf-8">
<title>Ferris Contracting – Business Card</title>
<link rel="stylesheet" href="https://fonts.googleapis.com/css2?family=Poppins:wght@400;600&family=Roboto:wght@400&display=swap">
<style>
  :root {
    --backdrop: #cfcfcf;
    --card: #000000;
    --blue: #2587bd;
    --blue-light: #3fa6de;
    --blue-dark: #1c74b6;
    --grey-band: #686868;
    --text-light: #f2f2f2;
    --rule: #9a9a9a;
  }
  * { box-sizing: border-box; margin: 0; padding: 0; }
  html, body {
    width: 956px;
    height: 1200px;
    overflow: hidden;
    background: var(--backdrop);
  }
  .card {
    position: absolute;
    left: 136px;
    width: 696px;
    height: 417px;
    background: var(--card);
    border-radius: 33px;
    overflow: hidden;
  }
  .card--front { top: 129px; }
  .card--back { top: 640px; }

  .card__bands {
    position: absolute;
    inset: 0;
    width: 100%;
    height: 100%;
  }

  .tab {
    position: absolute;
    left: 64px;
    top: 0;
    width: 25px;
    height: 107px;
    background: var(--blue);
  }
  .tab svg {
    position: absolute;
    left: 5px;
    bottom: 5px;
    width: 15px;
    height: 15px;
  }

  .identity {
    position: absolute;
    left: 64px;
    top: 116px;
    width: 198px;
  }
  .identity__name {
    font-family: "Poppins", sans-serif;
    font-size: 25px;
    line-height: 1.2;
    color: var(--text-light);
    font-weight: 400;
    letter-spacing: 0.2px;
    white-space: nowrap;
  }
  .identity__name strong { font-weight: 600; }
  .identity__role {
    font-family: "Roboto", sans-serif;
    font-size: 16px;
    color: var(--blue);
    margin-top: 1px;
  }
  .identity__rule {
    margin-top: 9px;
    height: 1px;
    background: var(--rule);
    position: relative;
  }
  .identity__rule::before {
    content: "";
    position: absolute;
    left: 0;
    top: -1px;
    width: 28px;
    height: 2px;
    background: var(--blue);
  }

  .contacts {
    position: absolute;
    left: 64px;
    top: 235px;
    list-style: none;
  }
  .contacts__item {
    display: flex;
    align-items: center;
    height: 24.5px;
    margin-bottom: 8px;
    font-family: "Poppins", sans-serif;
    font-size: 16.5px;
    color: var(--text-light);
  }
  .contacts__icon {
    width: 24.5px;
    height: 24.5px;
    background: var(--blue);
    margin-right: 11px;
    display: flex;
    align-items: center;
    justify-content: center;
    flex-shrink: 0;
  }
  .contacts__icon svg { width: 14px; height: 14px; }

  .wordmark {
    position: absolute;
    display: flex;
    align-items: center;
    gap: 12px;
    font-family: "Poppins", sans-serif;
    font-weight: 600;
    color: var(--blue-light);
    white-space: nowrap;
  }
  .wordmark__dot {
    width: 22px;
    height: 22px;
    border-radius: 50%;
    background: var(--blue-light);
    flex-shrink: 0;
  }
  .wordmark__text {
    display: flex;
    flex-direction: column;
    line-height: 1;
  }
  .wordmark__name { font-size: 50px; letter-spacing: 1px; }
  .wordmark__sub { font-size: 14px; letter-spacing: 7.5px; margin-top: 4px; }

  .card--front .wordmark { left: 384px; top: 163px; }
  .card--back .wordmark { left: 50%; top: 50%; transform: translate(-50%, -50%); }
</style>
</head>
<body>

<section class="card card--front" aria-label="Business card front">
  <svg class="card__bands" viewBox="0 0 696 417" preserveAspectRatio="none" aria-hidden="true">
    <defs>
      <linearGradient id="band-blue" x1="0" y1="0" x2="0" y2="1">
        <stop offset="0" stop-color="#1c6fae"/>
        <stop offset="0.45" stop-color="#40a8e0"/>
        <stop offset="1" stop-color="#1c74b6"/>
      </linearGradient>
    </defs>
    <polygon points="0,378 395,378 358,417 0,417" fill="var(--grey-band)"/>
    <polygon points="431,347 696,347 696,417 367,417" fill="url(#band-blue)"/>
  </svg>

  <div class="tab">
    <svg viewBox="0 0 16 16" aria-hidden="true">
      <circle cx="8" cy="5" r="3.2" fill="#fff"/>
      <path d="M1.5 15c0-3.6 2.9-5.6 6.5-5.6s6.5 2 6.5 5.6z" fill="#fff"/>
    </svg>
  </div>

  <div class="identity">
    <h1 class="identity__name"><strong>NAME</strong> SURNAME</h1>
    <p class="identity__role">Solution Manager</p>
    <div class="identity__rule"></div>
  </div>

  <ul class="contacts">
    <li class="contacts__item">
      <span class="contacts__icon">
        <svg viewBox="0 0 16 16" aria-hidden="true"><path d="M3.6 1.2l2.3 2.9-1.4 1.7c.9 2 2.5 3.6 4.5 4.6l1.7-1.4 2.9 2.3-1.3 2.6C6.9 13.8 2.2 9.1 1 3.8z" fill="#fff"/></svg>
      </span>
      +(000) 2457 8945
    </li>
    <li class="contacts__item">
      <span class="contacts__icon">
        <svg viewBox="0 0 16 16" aria-hidden="true"><rect x="1.5" y="3.5" width="13" height="9" fill="none" stroke="#fff" stroke-width="1.3"/><path d="M1.5 3.5L8 9l6.5-5.5M1.5 12.5L6 8m8.5 4.5L10 8" fill="none" stroke="#fff" stroke-width="1.3"/></svg>
      </span>
      info@company.com
    </li>
    <li class="contacts__item">
      <span class="contacts__icon">
        <svg viewBox="0 0 16 16" aria-hidden="true"><g fill="none" stroke="#fff" stroke-width="1"><circle cx="8" cy="8" r="6.3"/><ellipse cx="8" cy="8" rx="2.8" ry="6.3"/><path d="M1.7 8h12.6M2.6 4.8h10.8M2.6 11.2h10.8"/></g></svg>
      </span>
      www.company.com
    </li>
    <li class="contacts__item">
      <span class="contacts__icon">
        <svg viewBox="0 0 16 16" aria-hidden="true"><path d="M8 1.5L.8 7.6h2.1V14.5h3.6v-4h3v4h3.6V7.6h2.1z" fill="#fff"/></svg>
      </span>
      Address, Street 234, New Avenue
    </li>
  </ul>

  <div class="wordmark">
    <span class="wordmark__dot" aria-hidden="true"></span>
    <span class="wordmark__text">
      <span class="wordmark__name">FERRIS</span>
      <span class="wordmark__sub">CONTRACTING</span>
    </span>
  </div>
</section>

<section class="card card--back" aria-label="Business card back">
  <div class="wordmark">
    <span class="wordmark__dot" aria-hidden="true"></span>
    <span class="wordmark__text">
      <span class="wordmark__name">FERRIS</span>
      <span class="wordmark__sub">CONTRACTING</span>
    </span>
  </div>
</section>

</body>
</html>
```